Redesign of dating app main page

Task is redesign of main page of dating app. Page design is attached. UX design should be the same (buttons of the top of screen , scrolling down). Searching users profiles with their buttons should be more divided.

```html
<!DOCTYPE html>
<html lang="en">
<head>
<meta charset="utf-8">
<title>Dating App – Main Page</title>
<link rel="stylesheet" href="https://fonts.googleapis.com/css2?family=Roboto:wght@400;500;700&display=swap">
<style>
  :root {
    --bg-white: #ffffff;
    --bg-pink: #f2d6d6;
    --bg-mint: #ddefe0;
    --rule: #a58f95;
    --icon-grey: #9b9b9b;
    --card-border: #dcdcdc;
    --text-dark: #1e1e1e;
    --text-grey: #7a7a7a;
    --reject-red: #c22a31;
    --like-green: #6fcf7f;
    --dot-active: #8fd89a;
    --photo-main-a: #b9b9bc;
    --photo-main-b: #45454b;
    --photo-small-a: #c9c7c0;
    --photo-small-b: #8e8b7e;
  }
  * { box-sizing: border-box; margin: 0; padding: 0; }
  html, body { width: 1200px; height: 2598px; overflow: hidden; }
  body {
    position: relative;
    background: var(--bg-white);
    font-family: "Roboto", Arial, sans-serif;
    color: var(--text-dark);
  }
  .backdrop { position: absolute; left: 0; top: 0; width: 1200px; height: 2598px; }

  /* top navigation */
  .top-nav {
    position: absolute; left: 0; top: 0; width: 1200px; height: 216px;
    background: var(--bg-white);
    border-bottom: 3px solid var(--rule);
  }
  .nav-icon { position: absolute; top: 80px; width: 96px; height: 96px; }
  .nav-icon--profile { left: 48px; }
  .nav-icon--matches { left: 552px; }
  .nav-icon--messages { left: 1050px; }

  /* cards */
  .card {
    position: absolute;
    background: var(--bg-white);
    border: 4px solid var(--card-border);
    border-radius: 16px;
  }
  .card__photo { position: absolute; border-radius: 2px; }
  .dots {
    position: absolute; left: 0; right: 0;
    display: flex; justify-content: center;
  }
  .dot { border-radius: 50%; border: 4px solid #fff; }
  .dot--active { background: var(--dot-active); border-color: var(--dot-active); }

  /* featured profile */
  .card--featured { left: 112px; top: 320px; width: 998px; height: 1282px; }
  .featured__header {
    position: absolute; left: 44px; right: 36px; top: 30px;
    display: flex; align-items: baseline;
  }
  .featured__name { font-size: 56px; font-weight: 700; letter-spacing: 1px; }
  .featured__age { font-size: 52px; color: var(--text-grey); margin-left: 46px; }
  .featured__job { font-size: 49px; color: var(--text-grey); margin-left: 46px; }
  .featured__distance {
    margin-left: auto; display: flex; align-items: center;
    font-size: 40px; color: var(--text-grey);
  }
  .featured__distance svg { width: 34px; height: 46px; margin-right: 14px; align-self: center; }
  .card--featured .card__photo {
    left: 33px; top: 116px; width: 928px; height: 957px;
    background: linear-gradient(160deg, var(--photo-main-a) 0%, var(--photo-main-b) 100%);
  }
  .card--featured .dots { top: 1016px; gap: 50px; }
  .card--featured .dot { width: 28px; height: 28px; }
  .featured__actions {
    position: absolute; left: 44px; right: 44px; top: 1120px; height: 124px;
    display: flex; align-items: center; justify-content: space-between;
  }
  .action { width: 124px; height: 124px; }
  .see-more { font-size: 32px; font-weight: 500; letter-spacing: 2px; }

  /* profile grid */
  .card--small { width: 458px; height: 566px; }
  .card--col1 { left: 112px; }
  .card--col2 { left: 653px; }
  .card--row1 { top: 1661px; }
  .card--row2 { top: 2288px; }
  .small__header {
    position: absolute; left: 28px; right: 28px; top: 22px;
    display: flex; justify-content: space-between; align-items: baseline;
  }
  .small__name { font-size: 46px; font-weight: 500; letter-spacing: 1px; }
  .small__age { font-size: 44px; color: var(--text-dark); }
  .card--small .card__photo {
    left: 26px; top: 96px; width: 406px; height: 365px;
    background: linear-gradient(165deg, var(--photo-small-a) 0%, var(--photo-small-b) 100%);
  }
  .card--small .dots { top: 412px; gap: 34px; }
  .card--small .dot { width: 24px; height: 24px; border-width: 3px; }
  .small__actions {
    position: absolute; left: 30px; right: 30px; top: 476px; height: 68px;
    display: flex; align-items: center; justify-content: space-between;
  }
  .small__actions .action { width: 68px; height: 68px; }
  .small__job { font-size: 42px; color: var(--text-grey); }
</style>
</head>
<body>

<svg class="backdrop" viewBox="0 0 1200 2598" aria-hidden="true">
  <polygon points="0,216 1200,216 1200,952 0,760" fill="var(--bg-pink)"/>
  <path d="M0,1808 C300,1760 700,1690 1200,1730 L1200,2598 L0,2598 Z" fill="var(--bg-mint)"/>
</svg>

<header class="top-nav">
  <svg class="nav-icon nav-icon--profile" viewBox="0 0 32 32" aria-label="Profile">
    <circle cx="16" cy="10" r="7" fill="var(--icon-grey)"/>
    <path d="M2 30 C2 21 8 18 16 18 C24 18 30 21 30 30 Z" fill="var(--icon-grey)"/>
  </svg>
  <svg class="nav-icon nav-icon--matches" viewBox="0 0 32 32" aria-label="Matches">
    <path d="M16 2 C24 2 30 7.5 30 14 C30 20.5 24 26 16 26 L14 26 L9 31 L9 24.5 C4.5 22.3 2 18.5 2 14 C2 7.5 8 2 16 2 Z" fill="var(--icon-grey)"/>
    <path d="M16 20 L10.5 14.5 C8.7 12.7 9.6 9.5 12.3 9.5 C13.9 9.5 15.2 10.6 16 11.8 C16.8 10.6 18.1 9.5 19.7 9.5 C22.4 9.5 23.3 12.7 21.5 14.5 Z" fill="#fff"/>
  </svg>
  <svg class="nav-icon nav-icon--messages" viewBox="0 0 32 32" aria-label="Messages">
    <path d="M16 2 C24 2 30 7.5 30 14 C30 20.5 24 26 16 26 L14 26 L9 31 L9 24.5 C4.5 22.3 2 18.5 2 14 C2 7.5 8 2 16 2 Z" fill="var(--icon-grey)"/>
    <circle cx="10" cy="14" r="2" fill="#fff"/>
    <circle cx="16" cy="14" r="2" fill="#fff"/>
    <circle cx="22" cy="14" r="2" fill="#fff"/>
  </svg>
</header>

<main>
  <article class="card card--featured">
    <div class="featured__header">
      <span class="featured__name">LORA</span>
      <span class="featured__age">25</span>
      <span class="featured__job">Developer</span>
      <span class="featured__distance">
        <svg viewBox="0 0 12 16" aria-hidden="true"><path d="M6 0 C2.7 0 0 2.6 0 5.9 C0 10.3 6 16 6 16 C6 16 12 10.3 12 5.9 C12 2.6 9.3 0 6 0 Z" fill="var(--text-grey)"/><circle cx="6" cy="6" r="2.2" fill="#fff"/></svg>
        8 miles
      </span>
    </div>
    <div class="card__photo" role="img" aria-label="Profile photo of Lora"></div>
    <div class="dots">
      <span class="dot dot--active"></span><span class="dot"></span><span class="dot"></span><span class="dot"></span><span class="dot"></span>
    </div>
    <div class="featured__actions">
      <svg class="action" viewBox="0 0 40 40" aria-label="Pass">
        <circle cx="20" cy="20" r="18.5" fill="none" stroke="var(--reject-red)" stroke-width="2"/>
        <path d="M12.5 12.5 L27.5 27.5 M27.5 12.5 L12.5 27.5" stroke="var(--reject-red)" stroke-width="2.4" stroke-linecap="round"/>
      </svg>
      <span class="see-more">SEE MORE</span>
      <svg class="action" viewBox="0 0 40 40" aria-label="Like">
        <circle cx="20" cy="20" r="20" fill="var(--like-green)"/>
        <path d="M20 30 L11.5 21.5 C8.8 18.8 10.2 13 14.5 13 C17 13 18.8 14.6 20 16.4 C21.2 14.6 23 13 25.5 13 C29.8 13 31.2 18.8 28.5 21.5 Z" fill="#fff"/>
      </svg>
    </div>
  </article>

  <article class="card card--small card--col1 card--row1">
    <div class="small__header"><span class="small__name">SAM</span><span class="small__age">27</span></div>
    <div class="card__photo" role="img" aria-label="Profile photo of Sam"></div>
    <div class="dots">
      <span class="dot dot--active"></span><span class="dot"></span><span class="dot"></span><span class="dot"></span><span class="dot"></span>
    </div>
    <div class="small__actions">
      <svg class="action" viewBox="0 0 40 40" aria-label="Pass"><circle cx="20" cy="20" r="18" fill="none" stroke="var(--reject-red)" stroke-width="3"/><path d="M12.5 12.5 L27.5 27.5 M27.5 12.5 L12.5 27.5" stroke="var(--reject-red)" stroke-width="3.2" stroke-linecap="round"/></svg>
      <span class="small__job">Developer</span>
      <svg class="action" viewBox="0 0 40 40" aria-label="Like"><circle cx="20" cy="20" r="20" fill="var(--like-green)"/><path d="M20 30 L11.5 21.5 C8.8 18.8 10.2 13 14.5 13 C17 13 18.8 14.6 20 16.4 C21.2 14.6 23 13 25.5 13 C29.8 13 31.2 18.8 28.5 21.5 Z" fill="#fff"/></svg>
    </div>
  </article>

  <article class="card card--small card--col2 card--row1">
    <div class="small__header"><span class="small__name">PAULA</span><span class="small__age">22</span></div>
    <div class="card__photo" role="img" aria-label="Profile photo of Paula"></div>
    <div class="dots">
      <span class="dot dot--active"></span><span class="dot"></span><span class="dot"></span><span class="dot"></span><span class="dot"></span>
    </div>
    <div class="small__actions">
      <svg class="action" viewBox="0 0 40 40" aria-label="Pass"><circle cx="20" cy="20" r="18" fill="none" stroke="var(--reject-red)" stroke-width="3"/><path d="M12.5 12.5 L27.5 27.5 M27.5 12.5 L12.5 27.5" stroke="var(--reject-red)" stroke-width="3.2" stroke-linecap="round"/></svg>
      <span class="small__job">Developer</span>
      <svg class="action" viewBox="0 0 40 40" aria-label="Like"><circle cx="20" cy="20" r="20" fill="var(--like-green)"/><path d="M20 30 L11.5 21.5 C8.8 18.8 10.2 13 14.5 13 C17 13 18.8 14.6 20 16.4 C21.2 14.6 23 13 25.5 13 C29.8 13 31.2 18.8 28.5 21.5 Z" fill="#fff"/></svg>
    </div>
  </article>

  <article class="card card--small card--col1 card--row2">
    <div class="small__header"><span class="small__name">SAM</span><span class="small__age">27</span></div>
    <div class="card__photo" role="img" aria-label="Profile photo of Sam"></div>
  </article>

  <article class="card card--small card--col2 card--row2">
    <div class="small__header"><span class="small__name">PAULA</span><span class="small__age">22</span></div>
    <div class="card__photo" role="img" aria-label="Profile photo of Paula"></div>
  </article>
</main>

</body>
</html>
```